I have two swimming pool companies. I would like to combine them into one business card. They are both swimming pool service companies. One does residential (backyard pools) and the other does commercial (HOA, condo,apartment pools). I like the rounded edges on my cards, I am open to your ideas. I have two different websites for each.

www.brantmarine.com
www.oakridge-pools.com

Thanks!

Industry/Entity Type

Pool Service

Contact Information for Business Card

you decide, regular size, round, mini business card. Love all different designs. Don't have to use the "bubbles" from the old Brant Pool Service card design, but must use logos on the card. Could have one business on one side and another on the other. Or could do both on one side and services on the other.

Colors
0492cd
33a6d7
85cae6
cee9f5
eff8fb
eaf1f6
ceddec
85abd2
3176b5

Requirements
Must have
• Residential
• Commercial
• Repairs
• Replaster
• Liners
• Logos on the back of the card for brand recognition
• NWAK member
• MTG certified
• Residential Stewards Alliance
• Basin Dealers Guild
Should not have
• water as the background image or anywhere in the design.

```html
<!DOCTYPE html>
<html lang="en">
<head>
<meta charset="utf-8">
<title>Brant &amp; Oakridge Pool Business Cards</title>
<link rel="stylesheet" href="https://fonts.googleapis.com/css2?family=Open+Sans:wght@400;600;700;800&family=Cinzel:wght@400&display=swap">
<style>
  :root {
    --backdrop: #eef1f4;
    --metal-light: #ffffff;
    --metal-mid: #e2e4e7;
    --brand-blue: #2d6fb3;
    --navy: #1f3f8f;
    --text-muted: #3a5a86;
    --white: #ffffff;
  }
  * { box-sizing: border-box; margin: 0; padding: 0; }
  html, body { width: 1200px; height: 480px; overflow: hidden; }
  body { background: var(--backdrop); position: relative; font-family: "Open Sans", sans-serif; }

  .shared-defs { position: absolute; width: 0; height: 0; }

  .card {
    position: absolute;
    top: 94px;
    width: 480px;
    height: 270px;
    overflow: hidden;
    background:
      repeating-linear-gradient(0deg, rgba(0,0,0,0.025) 0 1px, transparent 1px 3px),
      linear-gradient(100deg, var(--metal-mid) 0%, var(--metal-light) 45%, var(--metal-mid) 100%);
    box-shadow: 3px 4px 8px rgba(0,0,0,0.25);
  }
  .card--residential { left: 84px; }
  .card--commercial { left: 636px; }

  .card__art { position: absolute; inset: 0; width: 480px; height: 270px; }

  .brand {
    position: absolute;
    left: 30px;
    top: 28px;
    width: 200px;
    color: var(--brand-blue);
    font-weight: 800;
    font-size: 28px;
    line-height: 1.05;
    display: flex;
    align-items: center;
    gap: 10px;
  }
  .card--commercial .brand { font-size: 25px; width: 215px; }
  .brand__dot { width: 20px; height: 20px; border-radius: 50%; background: var(--brand-blue); flex: none; }

  .offer {
    position: absolute;
    left: 30px;
    top: 118px;
    width: 190px;
    color: var(--text-muted);
    font-size: 11px;
    font-weight: 600;
    line-height: 16px;
  }

  .holder-name {
    position: absolute;
    left: 30px;
    bottom: 22px;
    font-family: "Cinzel", serif;
    font-size: 16px;
    letter-spacing: 0.5px;
    color: var(--navy);
  }

  .contact {
    position: absolute;
    right: 18px;
    top: 138px;
    text-align: right;
    color: var(--white);
    font-size: 12px;
    line-height: 19px;
  }
  .contact__company { font-weight: 700; font-size: 13px; }
  .contact__label { font-weight: 700; }
</style>
</head>
<body>

<svg class="shared-defs" aria-hidden="true">
  <defs>
    <linearGradient id="chevron-metal" x1="0" y1="0" x2="1" y2="0">
      <stop offset="0" stop-color="#9ea2a7"/>
      <stop offset="0.5" stop-color="#ffffff"/>
      <stop offset="1" stop-color="#c4c7cb"/>
    </linearGradient>
    <linearGradient id="panel-blue" x1="0" y1="0" x2="1" y2="1">
      <stop offset="0" stop-color="#3176b5"/>
      <stop offset="0.5" stop-color="#4a8ad0"/>
      <stop offset="1" stop-color="#2f6fb8"/>
    </linearGradient>
  </defs>
</svg>

<article class="card card--residential">
  <svg class="card__art" viewBox="0 0 480 270" aria-hidden="true">
    <polygon points="300,0 480,0 480,270 300,270 236,135" fill="url(#chevron-metal)"/>
    <polygon points="334,0 480,0 480,270 334,270 270,135" fill="url(#panel-blue)"/>
  </svg>
  <div class="brand"><span class="brand__dot"></span><span>Brant Pool Service</span></div>
  <div class="offer">
    <p>Residential · Commercial</p>
    <p>Repairs · Replaster · Liners</p>
  </div>
  <p class="holder-name">Your name here</p>
  <div class="contact">
    <p class="contact__company">Brant Pool Service,</p>
    <p class="contact__company">IncBrant</p>
    <p>Dalebrant@brantmarine.com</p>
    <p>www.brantmarine.com</p>
    <p><span class="contact__label">Tel:</span> 555-302-7100</p>
    <p><span class="contact__label">Fax:</span> 555-302-7199</p>
  </div>
</article>

<article class="card card--commercial">
  <svg class="card__art" viewBox="0 0 480 270" aria-hidden="true">
    <polygon points="300,0 480,0 480,270 300,270 236,135" fill="url(#chevron-metal)"/>
    <polygon points="334,0 480,0 480,270 334,270 270,135" fill="url(#panel-blue)"/>
  </svg>
  <div class="brand"><span class="brand__dot"></span><span>Oakridge Pool Management</span></div>
  <div class="offer">
    <p>NWAK member · MTG certified</p>
    <p>Residential Stewards Alliance</p>
    <p>Basin Dealers Guild</p>
  </div>
  <p class="holder-name">Your name here</p>
  <div class="contact">
    <p class="contact__company">Oakridge Pool</p>
    <p class="contact__company">Management</p>
    <p>Dalebrant@oakridge-pools.com</p>
    <p>www.oakridge-pools.com</p>
    <p><span class="contact__label">Tel:</span> 555-302-7100</p>
    <p><span class="contact__label">Fax:</span> 555-302-7199</p>
  </div>
</article>

</body>
</html>
```